Halvern Engineering HV - 740 - Twin Spinout flyer

I need a single page flyer, to advertise a product that i have manufactured. The name of the product is "HV - 740 Twin Spinout". i just want a few different pictures, title, small speal, list of features, my logo, all in the same colours as my logo.

The HV - 740 - Twin spinout is designed for the safe hands free breaking out of drill rods and Bottom hole assemblies between 4” and 20” in diameter. With a maximum passage of 520mm, all casing sizes up to 20" can easily pass through the breakout. With easily adjustable clamping pressures any thickness pipe can made up or broken without distortion. The making torque is also easily adjusted for correct make up torques.

Features are:
Designed, Engineered and Manufactured by Halvern Engineering
Compact design to allow for easy fitment
Maximum passage diameter is 520mm
Maximum clamping diameter id 20 inch
Minimum clamping diameter is 4 inch
Maximum breaking torque is 100,000 Nm

Thankyou

Gavin

Target Market(s)

Drilling Companies

Industry/Entity Type

Mechanical Engineering

Font styles to use
Sans Serif

Colors
0355a3
9bcb3c

Requirements
Must have
• various placed photos

```html
<!DOCTYPE html>
<html lang="en">
<head>
<meta charset="utf-8">
<title>Halvern Engineering HV - 740 - Twin Spinout flyer</title>
<link href="https://fonts.googleapis.com/css2?family=Arvo:wght@400;700&family=Lato:wght@300;400;700&display=swap" rel="stylesheet">
<style>
  :root {
    --page-bg: #e4e4e4;
    --paper: #ffffff;
    --green: #0cb13a;
    --blue: #0a3a9e;
    --ink: #1c1c1c;
    --white: #ffffff;
  }
  * { box-sizing: border-box; margin: 0; padding: 0; }
  html, body { width: 1200px; height: 1200px; overflow: hidden; }
  body {
    background: var(--page-bg);
    font-family: "Lato", sans-serif;
    color: var(--ink);
  }
  .flyer {
    position: absolute;
    left: 197px; top: 30px;
    width: 806px; height: 1141px;
    background: var(--paper);
    overflow: hidden;
  }
  .flyer__backdrop {
    position: absolute; inset: 0;
    width: 100%; height: 100%;
  }
  .headline {
    position: absolute;
    left: 30px; right: 30px; top: 70px;
    text-align: center;
    font-family: "Arvo", serif;
    font-weight: 400;
    font-size: 33px;
    line-height: 37.5px;
    color: var(--white);
  }
  .divider {
    position: absolute;
    height: 1.5px;
  }
  .divider::after {
    content: "";
    position: absolute;
    left: 50%; top: 50%;
    width: 13px; height: 13px;
    border-radius: 50%;
    transform: translate(-50%, -50%);
    background: inherit;
  }
  .divider--light { left: 88px; width: 620px; top: 292px; background: var(--white); }
  .divider--blue { left: 100px; width: 621px; top: 752px; background: var(--blue); }
  .intro {
    position: absolute;
    left: 72px; right: 72px; top: 320px;
    text-align: center;
    font-size: 22px;
    line-height: 29px;
    font-weight: 400;
    color: var(--white);
  }
  .gallery__photo {
    position: absolute;
    width: 196px; height: 196px;
    border-radius: 50%;
    border: 4px solid var(--blue);
    background: radial-gradient(circle at 40% 40%, #f1c21f 0%, #d9a514 55%, #6b5a2c 100%);
  }
  .gallery__photo--rig { left: 58px; top: 484px; }
  .gallery__photo--jaws { left: 303px; top: 484px; }
  .gallery__photo--cradle { left: 544px; top: 484px; }
  .features__title {
    position: absolute;
    left: 0; right: 0; top: 706px;
    text-align: center;
    font-family: "Arvo", serif;
    font-weight: 400;
    font-size: 26px;
    line-height: 32px;
    color: var(--ink);
  }
  .features__lead {
    position: absolute;
    left: 0; right: 0;
    text-align: center;
    font-family: "Arvo", serif;
    font-weight: 400;
    color: var(--ink);
  }
  .features__lead--maker { top: 769px; font-size: 20px; line-height: 28px; }
  .features__lead--compact { top: 799px; font-size: 24px; line-height: 30px; }
  .features__list {
    position: absolute;
    left: 0; right: 0; top: 840px;
    list-style: none;
    text-align: center;
    font-size: 19px;
    line-height: 25.8px;
    color: var(--ink);
  }
  .brand {
    position: absolute;
    left: 66px; top: 1018px;
    display: flex; align-items: center; gap: 18px;
  }
  .brand__mark {
    width: 62px; height: 62px;
    border-radius: 50%;
    background: var(--blue);
  }
  .brand__name {
    font-family: "Lato", sans-serif;
    font-weight: 700;
    font-size: 26px;
    line-height: 31px;
    color: var(--blue);
    text-transform: uppercase;
  }
  .contact {
    position: absolute;
    left: 430px; top: 992px;
    list-style: none;
    font-family: "Arvo", serif;
    color: var(--ink);
  }
  .contact__item { display: flex; align-items: center; gap: 14px; }
  .contact__item--phone { font-size: 36px; height: 44px; }
  .contact__item--mail, .contact__item--web { font-size: 21px; height: 35px; }
  .contact__icon { width: 20px; height: 22px; flex: none; }
</style>
</head>
<body>
<main class="flyer">
  <svg class="flyer__backdrop" viewBox="0 0 938 1327" preserveAspectRatio="none" aria-hidden="true">
    <defs>
      <linearGradient id="hero-green" x1="0" y1="0" x2="1" y2="1">
        <stop offset="0" stop-color="#1fc83c"/>
        <stop offset="0.6" stop-color="#0cb13a"/>
        <stop offset="1" stop-color="#089a33"/>
      </linearGradient>
    </defs>
    <path d="M0 594 Q180 680 470 688 Q720 690 938 640 L938 652 Q720 705 470 702 Q180 700 0 630 Z" fill="#111111"/>
    <path d="M0 0 H938 V640 Q720 690 470 688 Q180 680 0 594 Z" fill="url(#hero-green)"/>
  </svg>
  <div role="img" aria-label="Photo of the green-painted spinout unit behind the headline" style="position:absolute;inset:0 0 auto 0;height:560px;"></div>

  <h1 class="headline">The HV - 740 - Twin spinout<br>is designed for the safe hands free<br>breaking out of drill rods and Bottom<br>hole assemblies between 4” and 20”<br>in diameter.</h1>
  <div class="divider divider--light"></div>
  <p class="intro">With a maximum passage of 520mm, all casing sizes up to 20" can easily pass through the breakout. With easily adjustable clamping pressures any thickness pipe can made up or broken without distortion. The making torque is also easily adjusted for correct make up torques.</p>

  <div class="gallery__photo gallery__photo--rig" role="img" aria-label="Photo of the yellow spinout mounted on a drill rig with a rod through it"></div>
  <div class="gallery__photo gallery__photo--jaws" role="img" aria-label="Close-up photo of the steel clamping jaws inside the yellow body"></div>
  <div class="gallery__photo gallery__photo--cradle" role="img" aria-label="Photo of the open yellow clamp cradle from above"></div>

  <h2 class="features__title">FEATURES ARE:</h2>
  <div class="divider divider--blue"></div>
  <p class="features__lead features__lead--maker">Designed, Engineered and Manufactured by Halvern Engineering</p>
  <p class="features__lead features__lead--compact">Compact design to allow for easy fitment</p>
  <ul class="features__list">
    <li>Compact design to allow for easy fitment</li>
    <li>Maximum passage diameter is 520mm</li>
    <li>Maximum clamping diameter id 20 inch</li>
    <li>Minimum clamping diameter is 4 inch</li>
    <li>Maximum breaking torque is 100,000 Nm</li>
  </ul>

  <div class="brand">
    <span class="brand__mark"></span>
    <span class="brand__name">Halvern<br>Engineering</span>
  </div>

  <ul class="contact">
    <li class="contact__item contact__item--phone">
      <svg class="contact__icon" viewBox="0 0 20 28" aria-hidden="true"><rect x="3" y="1.5" width="14" height="25" rx="2.5" fill="none" stroke="#0a3a9e" stroke-width="2.4"/><line x1="8" y1="22.5" x2="12" y2="22.5" stroke="#0a3a9e" stroke-width="2"/></svg>
      (123) 456 789
    </li>
    <li class="contact__item contact__item--mail">
      <svg class="contact__icon" viewBox="0 0 22 22" aria-hidden="true"><rect x="1" y="5" width="20" height="13" fill="#0a3a9e"/><path d="M1 5 L11 12.5 L21 5" fill="none" stroke="#fff" stroke-width="1.6"/></svg>
      name@halvern20.com
    </li>
    <li class="contact__item contact__item--web">
      <svg class="contact__icon" viewBox="0 0 22 22" aria-hidden="true"><g fill="none" stroke="#0a3a9e" stroke-width="1.6"><circle cx="11" cy="11" r="9"/><ellipse cx="11" cy="11" rx="4" ry="9"/><line x1="2" y1="11" x2="20" y2="11"/><path d="M4 6 H18 M4 16 H18"/></g></svg>
      www.websitename.com
    </li>
  </ul>
</main>
</body>
</html>
```